Italian restaurant needs new site

Need to make our website better.

Must have reservation module

Must be able to sell wine tasting tours and wine pairing tours and intégrate with lumo desk

Blog

Social media

Wandermeter ranking and last review.

Number of Pages Required

1 page

Font styles to use
Serif

Requirements
Must have
• Reservation module
• Marketplace to buy wine pairings and gift certificates
• Wandermeter review
• Chatterbay posts
• All info from old site

```html
<!DOCTYPE html>
<html lang="en">
<head>
<meta charset="utf-8">
<title>Vellata Bistro — Italian Cuisine &amp; Wine Bar</title>
<link href="https://fonts.googleapis.com/css2?family=Noto+Serif:wght@400;700&family=Open+Sans:wght@400;600&display=swap" rel="stylesheet">
<style>
:root{
  --gold:#c9953f;
  --gold-dark:#b07f2e;
  --ink:#222;
  --text:#555;
  --white:#fff;
  --black:#0d0d0d;
  --dark:#1b1b1b;
  --footer:#3b3b3b;
  --footer-bottom:#2e2e2e;
  --light:#e6e6e6;
  --line:#999;
}
*{box-sizing:border-box;margin:0;padding:0}
html,body{width:1200px;height:5187px;overflow:hidden;background:var(--white)}
body{font-family:"Noto Serif",Georgia,serif;color:var(--ink)}
.page{position:relative;width:1200px;height:5187px;overflow:hidden}
.abs{position:absolute}
.btn-outline{position:absolute;border:2px solid var(--gold);color:var(--gold);font-size:17px;text-align:center;background:transparent}
.photo{position:absolute}

/* top bar */
.topbar{position:absolute;left:0;top:0;width:1200px;height:38px;background:var(--black);color:var(--white);font-family:"Open Sans",Arial,sans-serif;font-size:15px}
.topbar .item{position:absolute;top:9px;display:flex;align-items:center;gap:8px}
.topbar .social{position:absolute;left:770px;top:11px;display:flex;gap:20px}
.topbar .social span{width:16px;height:16px;border:1.5px solid var(--white);border-radius:3px}
.book-table{position:absolute;left:960px;top:0;width:190px;height:38px;background:var(--gold);color:var(--white);font-size:16px;line-height:38px;text-align:center;letter-spacing:1px}

/* hero */
.hero{position:absolute;left:0;top:38px;width:1200px;height:636px;background:radial-gradient(ellipse at 50% 35%,#6b4a30 0%,#3a2a1e 40%,#141110 80%)}
.brand{position:absolute;left:40px;top:70px;color:var(--white);text-align:center;width:180px}
.brand .mark{width:14px;height:14px;border-radius:50%;background:var(--white);margin:0 auto 8px}
.brand .name{font-size:30px;line-height:1.1}
.brand .tag{font-size:10px;letter-spacing:1px;margin-top:6px}
.nav{position:absolute;top:86px;left:355px;display:flex;gap:32px;color:var(--white);font-size:17px}
.hero-welcome{position:absolute;top:335px;width:100%;text-align:center;color:var(--white);font-size:36px;letter-spacing:2px}
.hero-title{position:absolute;top:395px;width:100%;text-align:center;color:var(--white);font-size:76px;letter-spacing:2px}
.hero-btn{position:absolute;left:465px;top:532px;width:270px;height:58px;border:2px solid var(--white);color:var(--white);font-size:19px;line-height:54px;text-align:center;letter-spacing:1px}

/* story */
.section-title{position:absolute;width:100%;text-align:center;font-size:42px;color:var(--gold)}
.story p{position:absolute;left:60px;width:1080px;text-align:center;font-size:18px;line-height:30px;color:var(--text)}
.story .hl{color:var(--gold)}

/* promotions */
.promos{position:absolute;left:0;top:1082px;width:1200px;height:491px;background:linear-gradient(#1c1814,#0e0c0a)}
.promos .title{position:absolute;top:22px;width:100%;text-align:center;color:var(--white);font-size:40px}
.promo{position:absolute;top:108px;height:370px}
.promo .photo{left:0;top:0;width:100%;height:248px}
.promo .label{position:absolute;top:266px;width:100%;text-align:center;color:var(--white);font-size:26px}
.promo .book{position:absolute;top:426px;left:50%;transform:translateX(-50%);width:82px;height:26px;border:1px solid var(--white);color:var(--white);font-family:"Open Sans",Arial,sans-serif;font-size:11px;line-height:24px;text-align:center;margin-top:-100px}

/* menu */
.menu-title{position:absolute;top:1620px;width:100%;text-align:center;font-size:46px;color:var(--ink)}
.menu-title .hl{color:var(--gold)}
.dish{position:absolute;text-align:center}
.dish .photo{position:relative;width:100%}
.dish .name{font-size:20px;color:var(--ink);margin-top:14px;line-height:24px}
.dish .price{font-size:21px;color:var(--gold);margin-top:8px}

/* reservation */
.reserve{position:absolute;left:0;top:2448px;width:1200px;height:439px;background:linear-gradient(#241d17,#120f0c)}
.reserve .title{position:absolute;top:20px;width:100%;text-align:center;color:var(--white);font-size:40px}
.field{position:absolute;width:310px;height:40px;border-bottom:1px solid #bbb;color:var(--white);font-size:15px}
.field span{position:absolute;left:0;top:10px}
.field svg{position:absolute;right:4px;top:8px}
.book-btn{position:absolute;left:478px;top:370px;width:200px;height:44px;border:2px solid var(--gold);color:var(--gold);font-size:18px;line-height:40px;text-align:center}

/* blog */
.blog{position:absolute;left:0;top:2887px;width:1200px;height:865px;background:var(--light)}
.blog .title{position:absolute;top:78px;width:100%;text-align:center;font-size:42px;color:var(--ink)}
.blog .title .hl{color:var(--gold)}
.post{position:absolute;top:180px;width:515px;height:650px}
.post .photo{left:0;top:0;width:515px;height:356px}
.post .ribbon{position:absolute;left:0;top:0;width:515px;height:36px;background:#8a1e17;color:var(--white);font-size:16px;line-height:36px;text-align:center;letter-spacing:1px}
.post .card{position:absolute;left:18px;top:305px;width:479px;height:345px;background:var(--white)}
.post .tag{position:absolute;left:139px;top:-20px;width:200px;height:44px;background:var(--gold);color:var(--white);font-size:21px;line-height:44px;text-align:center;letter-spacing:1px}
.post .body{position:absolute;left:36px;top:56px;width:400px;font-size:15px;line-height:25px;color:var(--ink)}
.post .divider{position:absolute;left:240px;top:205px;width:1px;height:90px;background:#ccc}
.post .meta{position:absolute;top:276px;font-size:14px}

/* reviews */
.rank-brand{position:absolute;top:3782px;width:100%;display:flex;justify-content:center;align-items:center;gap:10px;font-size:22px;color:var(--ink)}
.rank-brand i{width:26px;height:26px;border-radius:50%;background:var(--ink)}
.rank-title{position:absolute;top:3955px;width:100%;text-align:center;font-size:42px;color:var(--ink);letter-spacing:1px}
.rank-title .hl{color:var(--gold)}
.ranking{position:absolute;left:59px;top:4070px;width:512px;list-style:none}
.ranking li{height:55.5px;border-bottom:1.5px dashed var(--line);font-size:19px;line-height:55px;color:var(--ink)}
.ranking li.own{color:var(--gold)}
.ranking li:last-child{border-bottom:none}
.review{position:absolute;left:609px;top:4070px;width:560px;text-align:center}
.review .avatar{width:92px;height:92px;border-radius:50%;background:radial-gradient(circle,#e0894a,#7a3d1c);margin:0 auto}
.review .who{font-size:19px;color:var(--gold);margin-top:18px}
.review .where{font-size:19px;color:var(--ink);margin-top:6px}
.review .head{font-size:22px;color:var(--ink);margin-top:28px}
.review .text{font-size:15px;line-height:26px;color:var(--ink);margin-top:10px;text-align:left}
.dots{position:absolute;left:823px;top:4622px;display:flex;gap:14px}
.dots span{width:18px;height:18px;border-radius:50%;background:#ccc}
.dots span.on{background:var(--gold)}

/* footer */
.footer{position:absolute;left:0;top:4661px;width:1200px;height:474px;background:var(--footer);color:var(--white)}
.footer .ql-title{position:absolute;left:90px;top:30px;font-size:28px;color:var(--gold)}
.footer .links{position:absolute;left:95px;top:110px;list-style:none;font-size:15px;line-height:36px}
.footer .f-brand{position:absolute;left:440px;top:40px;width:320px;text-align:center}
.footer .f-brand .mark{width:16px;height:16px;border-radius:50%;background:var(--white);margin:0 auto 12px}
.footer .f-brand .name{font-size:40px}
.footer .f-brand .tag{font-size:12px;letter-spacing:1px;margin-top:6px}
.footer .contact{position:absolute;left:340px;width:520px;text-align:center;font-size:23px;color:var(--gold)}
.widget{position:absolute;left:840px;top:50px;width:322px;height:370px;background:var(--white);color:#333;font-family:"Open Sans",Arial,sans-serif}
.widget .cover{position:absolute;left:0;top:0;width:322px;height:150px;background:linear-gradient(135deg,#5a3a2a,#2a1c16)}
.widget .page-name{position:absolute;left:92px;top:22px;font-size:19px;color:var(--white)}
.widget .likes{position:absolute;left:92px;top:52px;font-size:13px;color:var(--white)}
.widget .thumb{position:absolute;left:14px;top:18px;width:66px;height:66px;background:#8a5a3a;border:2px solid var(--white)}
.widget .like-btn{position:absolute;left:92px;top:80px;width:150px;height:26px;background:#f2f2f2;border:1px solid #ccc;font-size:12px;line-height:24px;text-align:center}
.widget .friends{position:absolute;left:14px;top:168px;width:294px;font-size:13px;line-height:20px}
.widget .faces{position:absolute;left:14px;top:222px;display:flex;gap:6px}
.widget .faces span{width:40px;height:40px;background:#b8a89a}
.copyright{position:absolute;left:0;top:5135px;width:1200px;height:52px;background:var(--footer-bottom);color:#ddd;font-family:"Open Sans",Arial,sans-serif;font-size:12px;line-height:52px;text-align:center}
</style>
</head>
<body>
<div class="page">

  <!-- top bar -->
  <div class="topbar">
    <div class="item" style="left:14px">
      <svg width="16" height="16" viewBox="0 0 16 16"><circle cx="8" cy="8" r="7" fill="none" stroke="#fff" stroke-width="1.5"/><path d="M8 4v4l3 2" stroke="#fff" stroke-width="1.5" fill="none"/></svg>
      Opening Hours : 5 to 12 am (Everyday)
    </div>
    <div class="item" style="left:440px">
      <svg width="16" height="16" viewBox="0 0 16 16"><path d="M3 1h3l1.5 4-2 1.5a9 9 0 0 0 4 4l1.5-2 4 1.5v3a1 1 0 0 1-1 1A13 13 0 0 1 2 2a1 1 0 0 1 1-1z" fill="#fff"/></svg>
      Telephone : 555 0142
    </div>
    <div class="social"><span></span><span></span><span></span><span></span><span></span></div>
    <div class="book-table">BOOK A TABLE</div>
  </div>

  <!-- hero -->
  <section class="hero" role="img" aria-label="Grilled steak plated with roasted vegetables and a glass of wine on a dark restaurant table">
    <div class="brand">
      <div class="mark"></div>
      <div class="name">Vellata Bistro</div>
      <div class="tag">ITALIAN CUISINE &amp; WINE BAR</div>
    </div>
    <nav class="nav"><span>HOME</span><span>ABOUT US</span><span>MENU</span><span>RESERVATION</span><span>BLOG</span><span>WINE TOUR</span><span>CONTACT</span></nav>
    <div class="hero-welcome">WELCOME TO</div>
    <div class="hero-title">VELLATA BISTRO</div>
    <div class="hero-btn">RESERVATION NOW</div>
  </section>

  <!-- our story -->
  <section class="story">
    <h2 class="section-title" style="top:702px;font-weight:400">Our Story</h2>
    <p style="top:768px"><span class="hl">Vellata Bistro</span> Located in the heart of downtown, across from Plaza Alameda, just two short blocks up from Harborview Resort and the Cabo marina is Vellata Bistro, a place with great original Southern Italian and Mediterranean cuisine and a European touch.</p>
    <p style="top:866px">Sure to enjoy your classic favorites or satisfy even the most distinctive pallet We offer, a variety of home-made , fresh cooked dishes derived from generations-old family recipes, accompanied by an extensive upscale selection of national and international wines and fun Italian inspired cocktails.</p>
    <div class="btn-outline" style="left:534px;top:990px;width:140px;height:34px;line-height:30px">Read More</div>
  </section>

  <!-- promotions -->
  <section class="promos">
    <h2 class="title" style="font-weight:400">Special Promotions</h2>
    <div class="promo" style="left:28px;width:359px">
      <div class="photo" role="img" aria-label="Special dinner plate of grilled meat and vegetables" style="background:linear-gradient(135deg,#7a4a26,#3d2a18 60%,#5b6b2a)"></div>
      <div class="label">Special Dinner</div>
      <div class="book">Book Now</div>
    </div>
    <div class="promo" style="left:411px;width:370px">
      <div class="photo" role="img" aria-label="Weekend table spread with several dishes" style="background:linear-gradient(135deg,#8a5a34,#b88a5c 50%,#4a2e1c)"></div>
      <div class="label">Special Weekend</div>
      <div class="book">Book Now</div>
    </div>
    <div class="promo" style="left:806px;width:363px">
      <div class="photo" role="img" aria-label="Orange cocktail in a tall glass on the bar" style="background:linear-gradient(135deg,#c9712a,#e39a3e 50%,#5a2e14)"></div>
      <div class="label">Special Drinks</div>
      <div class="book">Book Now</div>
    </div>
  </section>

  <!-- menu -->
  <h2 class="menu-title" style="font-weight:400"><span class="hl">Delicious</span>&nbsp; Menu</h2>

  <div class="dish" style="left:59px;top:1722px;width:225px">
    <div class="photo" role="img" aria-label="Spanish tortilla slices on a plate" style="height:201px;background:linear-gradient(135deg,#e9dcc0,#c9a66a)"></div>
    <div class="name">Spanish-Tortilla</div><div class="price">$ 130</div>
  </div>
  <div class="dish" style="left:318px;top:1722px;width:235px">
    <div class="photo" role="img" aria-label="Bruschetta with smoked salmon" style="height:201px;background:linear-gradient(135deg,#e88a5a,#b8462a)"></div>
    <div class="name">Bruschetta Classica</div><div class="price">$ 120</div>
  </div>
  <div class="dish" style="left:588px;top:1722px;width:238px">
    <div class="photo" role="img" aria-label="Linguine with grilled shrimp" style="height:201px;background:linear-gradient(135deg,#d8a660,#8a5a2a)"></div>
    <div class="name">Linguine Imperiale</div><div class="price">$ 430</div>
  </div>
  <div class="dish" style="left:861px;top:1722px;width:287px">
    <div class="photo" role="img" aria-label="Spaghetti aglio olio with chili" style="height:201px;background:linear-gradient(135deg,#ecd79a,#c9a24e)"></div>
    <div class="name">Spaghetti Aglio olio<br>y peperoncino</div><div class="price" style="margin-top:0">$ 100</div>
  </div>

  <div class="dish" style="left:59px;top:2054px;width:225px">
    <div class="photo" role="img" aria-label="Bowl of minestrone soup" style="height:163px;background:linear-gradient(135deg,#d07040,#8a3a1a)"></div>
    <div class="name">Minestrone</div><div class="price">$ 120</div>
  </div>
  <div class="dish" style="left:318px;top:2054px;width:235px">
    <div class="photo" role="img" aria-label="Beef fillet skewers on a board" style="height:163px;background:linear-gradient(135deg,#a04a2a,#5a2414)"></div>
    <div class="name">Pinchos de Filete<br>de Res</div><div class="price" style="margin-top:0">$ 390</div>
  </div>
  <div class="dish" style="left:588px;top:2054px;width:238px">
    <div class="photo" role="img" aria-label="Cannoli dusted with sugar" style="height:163px;background:linear-gradient(135deg,#f0d8a8,#c99a5a)"></div>
    <div class="name">Cannoli de la Nona</div><div class="price">$ 90</div>
  </div>
  <div class="dish" style="left:861px;top:2054px;width:287px">
    <div class="photo" role="img" aria-label="Panna cotta with berry sauce" style="height:163px;background:linear-gradient(135deg,#f4eeea,#7a1a2a)"></div>
    <div class="name">Panna Cotta</div><div class="price">$ 80</div>
  </div>

  <div class="btn-outline" style="left:544px;top:2370px;width:134px;height:34px;line-height:30px">View More</div>

  <!-- reservation -->
  <section class="reserve" role="img" aria-label="Dim dining room with tables and chairs">
    <h2 class="title" style="font-weight:400">Reserve your seat Now</h2>
    <div class="field" style="left:68px;top:100px"><span>Your name</span>
      <svg width="20" height="20" viewBox="0 0 20 20"><circle cx="10" cy="6" r="4" fill="none" stroke="#fff" stroke-width="1.5"/><path d="M3 19c0-4 3-7 7-7s7 3 7 7" fill="none" stroke="#fff" stroke-width="1.5"/></svg></div>
    <div class="field" style="left:470px;top:100px"><span>Your phone</span>
      <svg width="20" height="20" viewBox="0 0 20 20"><circle cx="10" cy="10" r="9" fill="none" stroke="#fff" stroke-width="1.5"/><path d="M6 5h2l1 3-1.3 1a6 6 0 0 0 3 3L12 11l3 1v2a1 1 0 0 1-1 1A9 9 0 0 1 5 6a1 1 0 0 1 1-1z" fill="#fff"/></svg></div>
    <div class="field" style="left:830px;top:100px"><span>Your email</span>
      <svg width="22" height="20" viewBox="0 0 22 20"><rect x="1" y="4" width="20" height="13" fill="none" stroke="#fff" stroke-width="1.5"/><path d="M1 4l10 8 10-8" fill="none" stroke="#fff" stroke-width="1.5"/></svg></div>
    <div class="field" style="left:68px;top:255px"><span>Expected Date</span>
      <svg width="20" height="20" viewBox="0 0 20 20"><rect x="2" y="4" width="16" height="14" fill="none" stroke="#fff" stroke-width="1.5"/><path d="M2 8h16M6 2v4M14 2v4" stroke="#fff" stroke-width="1.5"/></svg></div>
    <div class="field" style="left:470px;top:255px"><span>Expected Time</span>
      <svg width="20" height="20" viewBox="0 0 20 20"><circle cx="10" cy="10" r="8" fill="none" stroke="#fff" stroke-width="1.5"/><path d="M10 5v5l3 2" stroke="#fff" stroke-width="1.5" fill="none"/></svg></div>
    <div class="field" style="left:830px;top:255px"><span>Total Person</span></div>
    <div class="book-btn">BOOK MY TABLE</div>
  </section>

  <!-- blog -->
  <section class="blog">
    <h2 class="title" style="font-weight:400">From The <span class="hl">BLOG</span></h2>
    <article class="post" style="left:59px">
      <div class="photo" role="img" aria-label="Platter of grilled seafood and vegetables" style="background:linear-gradient(135deg,#a86a3a,#5a3a20 50%,#c9a060)"></div>
      <div class="ribbon">ITALIAN &amp; MEDITERRANEAN CUISINE</div>
      <div class="card">
        <div class="tag">EVENTS</div>
        <p class="body">Lorem dolor sit amet, consectetur adipiscing elit. Morbi tempor ligula nec mauris tristique congue. Cras eget venenatis lectus. Donec sollicitudin eros est, quis maximus risus condimentum</p>
        <div class="divider"></div>
        <div class="meta" style="left:80px">25 June , 2017</div>
        <div class="meta" style="left:300px;color:var(--gold)">0 Comments</div>
      </div>
    </article>
    <article class="post" style="left:633px">
      <div class="photo" role="img" aria-label="Restaurant terrace lit up at night" style="background:linear-gradient(135deg,#3a2a20,#9a5a2a 50%,#2a1a12)"></div>
      <div class="ribbon">ITALIAN &amp; MEDITERRANEAN CUISINE</div>
      <div class="card">
        <div class="tag">WEEKENDS</div>
        <p class="body">Lorem dolor sit amet, consectetur adipiscing elit. Morbi tempor ligula nec mauris tristique congue. Cras eget venenatis lectus. Donec sollicitudin eros est, quis maximus risus condimentum</p>
        <div class="divider"></div>
        <div class="meta" style="left:80px">21 July, 2017</div>
        <div class="meta" style="left:300px;color:var(--gold)">0 Comments</div>
      </div>
    </article>
  </section>

  <!-- ranking & reviews -->
  <div class="rank-brand"><i></i>Wandermeter</div>
  <h2 class="rank-title" style="font-weight:400">RANKING <span class="hl">&amp;</span> REVIEWS</h2>
  <ol class="ranking">
    <li>#1 Serena - A Coastline Resort</li>
    <li>#2 Dunaluz Hotel and Resorts</li>
    <li>#3 Casa Brillante Resort &amp; Spa</li>
    <li>#4 Caleta Hotel &amp; Beach House</li>
    <li>#5 Mar Azul by Orvento</li>
    <li>#6 Villa Sereno Sunset Golf &amp; Spa Resort</li>
    <li>#7 Hotel Jardin Del Sol</li>
    <li>#8 Marisol Resort</li>
    <li class="own">#9 Vellata Bistro italian restaurant</li>
    <li>#10 Villa Sereno Los Cabos</li>
  </ol>
  <div class="review">
    <div class="avatar" role="img" aria-label="Reviewer profile picture"></div>
    <div class="who">SlowroadTravel</div>
    <div class="where">Austin, Texas</div>
    <div class="head">Magnificient Italian</div>
    <p class="text">The waitstaff were amazing. The food was incredible. It began with a sundried tomato wrapped around a kalamata olive stuffed with goat cheese, then on to a eggplant parmesan that was to die for. I had a greek salad and my companion had lasagna which were both terrific and the cap of the evening was a tiramasu out of this world. The next time we come back we've made a pack to dine there exclusively. There is literally no reason to eat anywhere else in Cabo San Lucas. The restaurant is beautiful with a ceiling fixed with bamboo and dark hued red woods abound topped with crisp white linens.</p>
  </div>
  <div class="dots"><span></span><span class="on"></span><span></span></div>

  <!-- footer -->
  <footer class="footer">
    <div class="ql-title">Quick Links</div>
    <ul class="links"><li>HOME</li><li>ABOUT US</li><li>RESERVATION</li><li>MENU</li><li>BLOG</li><li>WINE TOUR</li><li>CONTACT US</li></ul>
    <div class="f-brand">
      <div class="mark"></div>
      <div class="name">Vellata Bistro</div>
      <div class="tag">ITALIAN CUISINE &amp; WINE BAR</div>
    </div>
    <div class="contact" style="top:200px">Telephone :&nbsp; 555 0142</div>
    <div class="contact" style="top:245px">Email : contact@vellatabistro.com</div>
    <div class="contact" style="top:295px">open daily from 5 to 12 am</div>
    <div class="widget">
      <div class="cover" role="img" aria-label="Restaurant page cover photo"></div>
      <div class="thumb"></div>
      <div class="page-name">Vellata Bistro</div>
      <div class="likes">3.460 Me gusta</div>
      <div class="like-btn">Me gusta esta página</div>
      <p class="friends">Sé el primero de tus amigos en indicar que te gusta esto</p>
      <div class="faces"><span></span><span></span><span></span><span></span><span></span><span></span></div>
    </div>
  </footer>
  <div class="copyright">copyright 2017 Vellata Bistro . All rights reserved</div>

</div>
</body>
</html>
```